Residential improvers, A Quiet Harbor 9 Me *

Quiet Harbor 9 Me is a real estate company specializing in turning unloved properties into improved, happy places to live. We specialize in thoughtfully-improved residential properties for buyers or renters. Our company needs a business card that reflects the renovated homes we create using green and Feng Shui principles,

Please disregard the images we submitted. We are looking for an abstract, sophisticated elegant design. No eggs in a nest ... nothing cute. The image can be soft.
Updates

Aloha (hello) all designers. We are a serious property investment/improvement company. We strive to be unique, renovating with style and elegance. Our business card must portray the same message. We thought the nest and flower might be "it" ... clearly it's not, once we saw what you submitted. Please revisit the brief as it was modified yesterday. Mahalo for your input! We look forward to hearing from all designers that have been invited.

Industry/Entity Type

Real Estate Development

Contact Information for Business Card

We will have separate business cards for
1) Corabeth Danvers 808-555-0173 corabeth@mailtrove.net
2) Trina Vasquell 808-555-0196 trinavasquell@mailtrove.net
** can we add the website later ... in the process of approval.
Investors * Renovators * Connectors

Font styles to use
Sans Serif

Colors
cadf82

Requirements
Must have
• a feng shui feel ... modern. Color - green with black print.
Nice to have
• A Quiet Harbor 9 Me

```html
<!DOCTYPE html>
<html lang="en">
<head>
<meta charset="utf-8">
<title>A Quiet Harbor 9 Me — Business Card</title>
<link rel="stylesheet" href="https://fonts.googleapis.com/css2?family=Questrial&display=swap">
<style>
  :root {
    --backdrop: #2c3037;
    --card-white: #ffffff;
    --card-black: #0b0b0b;
    --ink: #1f1f1f;
    --ink-light: #f2f2f2;
    --green-deep: #2f8a1e;
    --green-mid: #5aa832;
    --green-lime: #cadf82;
    --green-bright: #c9dd3a;
  }
  * { margin: 0; padding: 0; box-sizing: border-box; }
  html, body {
    width: 1200px; height: 900px; overflow: hidden;
    background: var(--backdrop);
    font-family: "Questrial", "Century Gothic", sans-serif;
  }
  .canvas { position: relative; width: 1200px; height: 900px; }

  .card {
    position: absolute; width: 630px; height: 360px;
    border-radius: 4px;
    box-shadow: 0 14px 30px rgba(0,0,0,.45);
    overflow: hidden;
  }
  .card--front { left: 120px; top: 440px; background: var(--card-white); }
  .card--back  { left: 450px; top: 90px;  background: var(--card-black); }

  /* company name, set as plain text */
  .company-name {
    position: absolute; font-size: 27px; line-height: 1.2;
    letter-spacing: .2px; white-space: nowrap;
  }
  .card--front .company-name { left: 40px; top: 40px; color: var(--ink); }
  .card--back  .company-name { left: 0; right: 0; top: 150px; text-align: center; color: var(--ink-light); }

  /* service line, kept apart from the name */
  .services {
    position: absolute; font-size: 13px; line-height: 1.2;
    color: var(--green-mid); letter-spacing: .3px; white-space: nowrap;
  }
  .card--front .services { left: 40px; top: 222px; }
  .card--back  .services { left: 0; right: 0; bottom: 36px; text-align: center; color: var(--green-lime); }

  /* person */
  .person { position: absolute; right: 44px; top: 146px; text-align: right; }
  .person__name { font-size: 27px; line-height: 1.2; color: var(--ink); }
  .person__title { font-size: 15px; line-height: 1.2; color: var(--green-mid); margin-top: 4px; }

  .divider {
    position: absolute; left: 40px; right: 40px; top: 248px; height: 1px;
    background: linear-gradient(90deg, var(--green-deep), var(--green-bright));
  }

  .contacts {
    position: absolute; left: 40px; right: 40px; top: 270px;
    display: flex; justify-content: space-between; list-style: none;
  }
  .contact { display: flex; align-items: center; gap: 9px; font-size: 14px; color: var(--ink); white-space: nowrap; }
  .contact__icon { width: 22px; height: 22px; flex: none; }

  .band {
    position: absolute; left: 0; right: 0; bottom: 0; height: 20px;
    background: linear-gradient(90deg, var(--green-deep), var(--green-mid) 45%, var(--green-bright));
  }
</style>
</head>
<body>
<main class="canvas">

  <section class="card card--back" aria-label="Card back">
    <p class="company-name">A Quiet Harbor 9 Me</p>
    <p class="services">Investors • Renovators • Connectors</p>
  </section>

  <section class="card card--front" aria-label="Card front">
    <p class="company-name">A Quiet Harbor 9 Me</p>

    <div class="person">
      <p class="person__name">Corabeth Danvers</p>
      <p class="person__title">Managing Director</p>
    </div>

    <p class="services">Investors • Renovators • Connectors</p>

    <div class="divider"></div>

    <ul class="contacts">
      <li class="contact">
        <svg class="contact__icon" viewBox="0 0 22 22" aria-hidden="true">
          <circle cx="11" cy="11" r="10" fill="none" stroke="#5aa832" stroke-width="1.5"/>
          <path d="M8 6.5c-.8.4-1.3 1.2-1 2.4.6 2.6 2.8 5 5.4 5.9 1.1.4 2 0 2.5-.8l-1.8-1.6-1.2.8c-1.2-.6-2.1-1.6-2.6-2.8l.8-1.1L8 6.5z" fill="#5aa832"/>
        </svg>
        <span>808-555-0173</span>
      </li>
      <li class="contact">
        <svg class="contact__icon" viewBox="0 0 22 22" aria-hidden="true">
          <circle cx="11" cy="11" r="10" fill="none" stroke="#5aa832" stroke-width="1.5"/>
          <rect x="6" y="7.5" width="10" height="7" rx="1" fill="#5aa832"/>
          <path d="M6.5 8l4.5 3.6L15.5 8" fill="none" stroke="#fff" stroke-width="1"/>
        </svg>
        <span>corabeth@mailtrove.net</span>
      </li>
      <li class="contact">
        <svg class="contact__icon" viewBox="0 0 22 22" aria-hidden="true">
          <circle cx="11" cy="11" r="10" fill="none" stroke="#5aa832" stroke-width="1.5"/>
          <circle cx="11" cy="11" r="5.5" fill="none" stroke="#5aa832" stroke-width="1.2"/>
          <ellipse cx="11" cy="11" rx="2.4" ry="5.5" fill="none" stroke="#5aa832" stroke-width="1"/>
          <path d="M5.5 11h11M6.4 8.3h9.2M6.4 13.7h9.2" stroke="#5aa832" stroke-width="1"/>
        </svg>
        <span>aquietharbor9me.com</span>
      </li>
    </ul>

    <div class="band"></div>
  </section>

</main>
</body>
</html>
```